Tea Shop - Drinks Menu - Vertical TV screen

Need a drinks menu design for a tea shop based in The Netherlands. Called BrewHaven.
Currently we are trying to attract more customers for our SipAway and the idea came up to place 3 TV screen vertically in order to use 2 for the menu.
Website: http://brewhaven-velden.example.nl/
Posible colour themes -
- Light green (same green as logo)
- Light brown
Dimensions of the screen -
- 40inch
- 905 mm Height
- 207 mm Width
Resolution of the menu must be 1920x1080 BUT VERTICAL
Needs to contain the following -
- Hot SipAway
- BLACK
- Delicate Earl Grey
- Golden Sun Kiss
- Rosy Orchard
- Spicy Chai
- Black Assam
- Duchess of Hills
- Smokey Lapsang Suochong
- ( and many more teas, so leave space for aditional 5+)
- GREEN
- Sencha Lime-Ginger
- Sencha Forest Berries
- Sencha Orange Choco
- Happy Blossom
- Bancha
- Classic Gunpowder
- (space for aditional 4+)
- OOLONG
- Bullet Oolong
- Milky Oolong
- WHITE
- Bai Mu Tan
- HERBAL
- BrewHaven's Cloud
- Revitalising Kamille
- Pure Ginger
- Moon Blend
- Nana Mint
- Basil Strawberry
- FRUIT TEA
- Fruity Almond
- Berry Jolly
- Papaya Hug
- Spicy Pear
- Turkish Apple
- (space for aditional 2+)
- LATTÉ
- Spiced Chai
- Green Chai
- Vanille Chai
- Matcha
- Fresh Mint tea
- Iced Tea
- Peach
- Raspberry
- Lemon
- Mango
Divide this menu over 2 TV screens with the mentioned dimensions and use the font provided in the uploaded files (not mandatory if you think you have a bette idea).
Simple
Needs to attract people
Easy to adjust
Idea's are always welcome and appreciated
LOGO LINK : http://img.pictobox.example/7kq4zr9.png
(image too big to upload on here, sorry)
Target Market(s)
people whom drink TEA
Industry/Entity Type
Tv

```html
<!DOCTYPE html>
<html lang="en">
<head>
<meta charset="utf-8">
<title>Hot SipAway – BrewHaven Menu</title>
<link rel="stylesheet" href="https://fonts.googleapis.com/css2?family=Fredoka:wght@500;600&family=Montserrat:wght@600;700&display=swap">
<style>
  :root {
    --paper-light: #f0dfa8;
    --paper-mid: #e3c98a;
    --paper-warm: #c99a5a;
    --rust: #a2582a;
    --leaf-green: #4a7a2c;
    --ink: #2b2418;
    --bullet-ring: #c8743a;
    --band: rgba(255, 250, 230, 0.45);
    --white: #ffffff;
  }
  * { margin: 0; padding: 0; box-sizing: border-box; }
  html, body { width: 675px; height: 1200px; overflow: hidden; }
  body { background: var(--paper-mid); }
  .menu-screen {
    position: relative;
    width: 675px;
    height: 1200px;
    overflow: hidden;
    background:
      radial-gradient(ellipse 420px 260px at 60% 60px, rgba(162, 88, 42, 0.55), transparent 70%),
      radial-gradient(ellipse 260px 420px at 0 180px, rgba(201, 154, 90, 0.6), transparent 70%),
      linear-gradient(180deg, var(--paper-warm) 0%, var(--paper-mid) 22%, var(--paper-light) 55%, var(--paper-mid) 100%);
    font-family: "Fredoka", sans-serif;
    color: var(--ink);
  }
  .header-art {
    position: absolute;
    left: 0; top: 0;
    width: 675px; height: 150px;
    background: radial-gradient(ellipse 300px 130px at 55% 80px, rgba(120, 70, 30, 0.35), transparent 75%);
  }
  .menu-title {
    position: absolute;
    top: 44px; left: 0; width: 100%;
    text-align: center;
    font-family: "Montserrat", sans-serif;
    font-weight: 700;
    font-size: 82px;
    line-height: 96px;
    letter-spacing: -1px;
    color: var(--white);
    text-shadow: 0 2px 6px rgba(90, 50, 20, 0.35);
  }
  .category-band {
    position: absolute;
    left: 32px; width: 600px; height: 46px;
    background: linear-gradient(90deg, var(--band), rgba(255, 250, 230, 0.3) 80%, transparent);
  }
  .category-band.black-oolong { top: 160px; }
  .category-band.green-white { top: 646px; }
  .category-title {
    position: absolute;
    font-family: "Montserrat", sans-serif;
    font-weight: 700;
    font-size: 35px;
    line-height: 46px;
    color: var(--leaf-green);
  }
  .category-title.rounded { font-family: "Fredoka", sans-serif; font-weight: 600; }
  .tea-list {
    position: absolute;
    list-style: none;
  }
  .tea-item {
    display: flex;
    align-items: center;
    height: 34.8px;
    font-size: 28px;
    font-weight: 500;
    white-space: nowrap;
  }
  .tea-item::before {
    content: "";
    flex: none;
    width: 14px; height: 14px;
    margin-right: 9px;
    border-radius: 50%;
    border: 3px solid var(--bullet-ring);
    background: var(--white);
  }
  .tea-list.black { left: 26px; top: 224px; }
  .tea-list.oolong { left: 392px; top: 224px; }
  .tea-list.green { left: 26px; top: 701px; }
  .tea-list.green .tea-item { height: 34px; }
  .tea-list.green .tea-item.slot { height: 35px; }
  .tea-single {
    position: absolute;
    left: 450px; top: 713px;
    font-size: 28px;
    font-weight: 500;
    line-height: 34px;
  }
  .drinks-photo {
    position: absolute;
    left: 0; top: 900px;
    width: 675px; height: 300px;
    background: linear-gradient(180deg, rgba(200, 170, 120, 0) 0%, rgba(186, 150, 100, 0.55) 30%, rgba(140, 100, 60, 0.75) 100%);
  }
</style>
</head>
<body>
  <main class="menu-screen">
    <div class="header-art" role="img" aria-label="Loose tea leaves on a scoop with swirling ornaments"></div>
    <h1 class="menu-title">Hot SipAway</h1>

    <div class="category-band black-oolong"></div>
    <h2 class="category-title" style="left:58px; top:162px;">BLACK</h2>
    <h2 class="category-title rounded" style="left:421px; top:158px;">OOLONG</h2>

    <ul class="tea-list black">
      <li class="tea-item">Delicate Earl Grey</li>
      <li class="tea-item">Golden Sun Kiss</li>
      <li class="tea-item">Rosy Orchard</li>
      <li class="tea-item">Spicy Chai</li>
      <li class="tea-item">Black Assam</li>
      <li class="tea-item">Duchess of Hills</li>
      <li class="tea-item">Smokey Lapsang Suochong</li>
      <li class="tea-item slot"></li>
      <li class="tea-item slot"></li>
      <li class="tea-item slot"></li>
      <li class="tea-item slot"></li>
      <li class="tea-item slot"></li>
    </ul>

    <ul class="tea-list oolong">
      <li class="tea-item">Bullet Oolong</li>
      <li class="tea-item">Milky Oolong</li>
    </ul>

    <div class="drinks-photo" role="img" aria-label="Take-away tea cups with BrewHaven sleeves and an iced tea with a pink straw"></div>

    <div class="category-band green-white"></div>
    <h2 class="category-title" style="left:59px; top:651px;">GREEN</h2>
    <h2 class="category-title" style="left:454px; top:651px;">WHITE</h2>

    <ul class="tea-list green">
      <li class="tea-item">Sencha Lime-Ginger</li>
      <li class="tea-item">Sencha Forest Berries</li>
      <li class="tea-item">Sencha Orange Choco</li>
      <li class="tea-item">Happy Blossom</li>
      <li class="tea-item">Bancha</li>
      <li class="tea-item">Classic Gunpowder</li>
      <li class="tea-item slot"></li>
      <li class="tea-item slot"></li>
      <li class="tea-item slot"></li>
      <li class="tea-item slot"></li>
    </ul>

    <p class="tea-single">Bai Mu Tan</p>
  </main>
</body>
</html>
```